Wix web design for healthcare IT consulting firm.

I am looking for a web design built in Wix that it will be easy for me to add or edit content in the future. The web site does not need to be overly complicated, but it should look very polished and professional. I also want to ensure it is mobile device friendly. I do not need any type of on-line purchasing ability. I will eventually do blogs, but for now it is a fairly standard web site with main page, about us, services provided, etc. I would also like a place for potential customers to contact us directly from the web site. I have included a Word document with some content for the web design. I have also included my logo and business card for reference. I would like to utilize similar colors as my business card. One of my primary competitors is https://vontalmhc.example/

Target Market(s)

Target market could be nursing home CEO, CIO, or other leader at an organization that manages long term care facilities.

Number of Pages Required

5+ page

Colors
876aae

Requirements
Must have
• Be designed to be used in Wix. Use the content I provided to create and make web design. Allow to be viewed on mobile device. Please use similar color structure as attached business card. Please use attached logo in design.

```html
<!DOCTYPE html>
<html lang="en">
<head>
<meta charset="utf-8">
<title>Cardella Health Advisors</title>
<link rel="stylesheet" href="https://fonts.googleapis.com/css2?family=Poppins:wght@400;500;600&family=Roboto:wght@400;500;700&display=swap">
<style>
:root{
  --purple:#6a3fae;
  --purple-dark:#54309a;
  --purple-soft:#876aae;
  --ink:#1b1b1b;
  --text:#555;
  --muted:#8a8a8a;
  --light:#f3f3f3;
  --dark:#1f1f22;
  --white:#fff;
}
*{box-sizing:border-box;margin:0;padding:0}
html,body{width:1200px;height:3896px;overflow:hidden}
body{font-family:"Poppins",sans-serif;color:var(--text);background:var(--white);position:relative;font-size:12px}
section,header,footer{position:absolute;left:0;width:1200px}
.abs{position:absolute}
h2{font-family:"Roboto",sans-serif;font-weight:700;color:var(--ink);font-size:32px}
h2 em{font-style:normal;color:var(--purple)}
.btn{display:inline-block;font-size:10px;font-weight:600;letter-spacing:.5px;color:var(--white);background:var(--purple);padding:10px 18px;text-transform:uppercase;white-space:nowrap}
.ph{position:absolute}

/* header */
.site-header{top:0;height:78px;background:var(--purple)}
.brand{left:210px;top:10px;height:58px;display:flex;align-items:center;gap:8px;font-family:"Poppins",sans-serif;font-weight:600;font-size:26px;color:var(--white)}
.brand i{width:10px;height:10px;background:var(--white);display:block}
.topinfo{top:6px;right:210px;display:flex;gap:24px;align-items:center;font-size:10px;color:var(--white)}
.topinfo span{display:flex;align-items:center;gap:6px}
.search{width:140px;height:20px;border:1px solid rgba(255,255,255,.5);background:var(--purple-dark);font-size:9px;padding:3px 8px;color:rgba(255,255,255,.7)}
.nav{top:40px;left:445px;display:flex;gap:28px;font-size:11px;font-weight:500;color:var(--white)}
.nav a{padding:6px 10px;color:inherit;text-decoration:none}
.nav a.active{border:1px solid rgba(255,255,255,.7);background:rgba(255,255,255,.12)}

/* hero */
.hero{top:78px;height:532px;background:linear-gradient(110deg,#8fb3c7 0%,#d8e2e8 35%,#eef2f4 55%,#9aa8b4 80%,#5c6570 100%)}
.hero-box{left:268px;top:195px;width:662px;height:156px;background:rgba(106,63,174,.9);border:2px solid rgba(255,255,255,.5);text-align:center;padding-top:24px}
.hero-box h1{font-family:"Roboto",sans-serif;font-weight:700;font-size:33px;line-height:44px;color:var(--white)}
.hero-btns{left:0;right:0;top:324px;display:flex;justify-content:center;gap:8px}
.hero-btns .btn{border:1px solid var(--white);padding:10px 22px}
.hero-btns .btn.black{background:#111;border-color:#111}
.arrow{width:28px;height:28px;background:var(--purple);display:flex;align-items:center;justify-content:center}
.values{top:610px;height:148px;background:#0d0d0f}
.value{position:absolute;top:-33px;width:122px;text-align:center;color:var(--white);font-size:12px;font-weight:500;line-height:15px}
.value .tile{width:122px;height:103px;background:var(--purple);border:2px solid rgba(255,255,255,.6);display:flex;align-items:center;justify-content:center;margin-bottom:10px}

/* welcome */
.welcome{top:758px;height:398px}
.welcome p{font-size:11px;line-height:20px}

/* services */
.services{top:1156px;height:610px;background:linear-gradient(180deg,#7a55bb,#6a3fae 60%,#6b45ad)}
.services .intro{left:210px;width:780px;top:112px;text-align:center;color:rgba(255,255,255,.85);font-size:11px;line-height:18px}
.svc h3{font-family:"Roboto",sans-serif;font-size:15px;color:var(--white);font-weight:700;margin-bottom:12px}
.svc li{list-style:none;color:var(--white);font-size:11px;line-height:27px;display:flex;align-items:center;gap:8px}
.svc .more{color:var(--white);font-size:10px;font-weight:600;text-decoration:underline;margin-top:8px;display:block}

/* leadership */
.leaders{top:1766px;height:462px}
.bio{left:520px;top:120px;width:470px;font-size:11px;line-height:20px}
.bio b{color:var(--ink);font-size:12px}
.thumb{position:absolute;top:290px;width:145px;text-align:center;font-size:11px;font-weight:600;color:var(--ink)}
.thumb .ph{position:relative;height:90px;margin-bottom:12px}

/* testimonials */
.clients{top:2228px;height:351px;background:linear-gradient(90deg,#2a2a2e,#3a3a40 50%,#26262a)}
.quote{position:absolute;top:156px;width:345px;height:140px;background:var(--white);padding:16px 20px 0 110px;font-size:10px;line-height:17px}
.quote .ph{left:20px;top:-16px;width:70px;height:70px;border:3px solid var(--white)}
.quote .who{color:var(--purple);font-weight:600;font-size:10px;margin-top:6px}

/* approach */
.approach{top:2579px;height:428px;background:var(--light)}
.approach .left{left:0;top:0;width:600px;height:428px;background:linear-gradient(120deg,#7c58b7,#6a3fae)}
.pill{position:absolute;left:545px;display:flex;align-items:center;gap:28px}
.pill .sq{width:110px;height:92px;background:#000;display:flex;align-items:center;justify-content:center}
.pill p{font-family:"Roboto",sans-serif;font-weight:500;font-size:17px;line-height:22px;color:var(--ink)}

/* blog */
.blog{top:3007px;height:525px}
.card{position:absolute;top:102px;width:239px;height:314px;background:var(--white);box-shadow:0 2px 8px rgba(0,0,0,.15);text-align:center}
.card .ph{left:0;top:0;width:239px;height:168px}
.card .date{position:absolute;right:12px;top:0;width:40px;height:52px;background:#111;color:var(--white);font-family:"Roboto",sans-serif;font-weight:700;font-size:17px;line-height:24px;padding-top:4px}
.card .date small{display:block;font-size:9px;line-height:10px;background:var(--white);color:var(--ink);margin:2px 4px 0}
.card h4{margin-top:186px;font-family:"Roboto",sans-serif;font-size:13px;line-height:18px;color:var(--ink);font-weight:700;padding:0 20px}
.card p{font-size:10px;line-height:17px;color:var(--muted);padding:10px 22px 0}
.card .corner{position:absolute;right:0;bottom:0;width:0;height:0;border-left:34px solid transparent;border-bottom:34px solid #111}
.card .corner.p{border-bottom-color:var(--purple)}

/* footer */
.site-footer{top:3532px;height:364px;background:linear-gradient(90deg,#1a1a1c,#2b2b30 50%,#1a1a1c)}
.site-footer h3{font-family:"Roboto",sans-serif;color:var(--white);font-size:19px;font-weight:700}
.field{position:absolute;left:210px;width:215px;height:30px;background:var(--white);font-size:9px;color:var(--muted);padding:8px 10px}
.contact-row{position:absolute;left:710px;display:flex;gap:14px;color:var(--white)}
.contact-row b{font-size:11px;font-weight:600;display:block}
.contact-row span{font-size:10px;color:#bbb}
.bottom-bar{left:0;top:330px;width:1200px;height:34px;background:var(--purple);color:var(--white);font-size:9px}
.social{display:flex;gap:6px}
.social i{width:18px;height:18px;border-radius:50%;background:var(--white);display:block}
</style>
</head>
<body>

<header class="site-header">
  <div class="brand abs"><i></i>Cardella</div>
  <div class="topinfo abs">
    <span><svg width="12" height="12" viewBox="0 0 24 24"><rect x="1" y="1" width="22" height="22" fill="#fff"/><path d="M8 5l3 4-2 2c1 2 3 4 5 5l2-2 4 3-2 3C11 20 4 13 5 7z" fill="#6a3fae"/></svg>555-014-2290</span>
    <span><svg width="12" height="12" viewBox="0 0 24 24"><rect x="1" y="1" width="22" height="22" fill="#fff"/><path d="M4 7h16v10H4zM4 7l8 6 8-6" fill="none" stroke="#6a3fae" stroke-width="2"/></svg>gellison@cardellahealth.example</span>
    <div class="search">Search</div>
  </div>
  <nav class="nav abs">
    <a class="active">HOME</a><a>ABOUT US</a><a>OUR SERVICES ▾</a><a>BLOG</a><a>CAREERS</a><a>CONTACT US</a>
  </nav>
</header>

<section class="hero">
  <div class="ph" role="img" aria-label="Photo of a doctor with stethoscope and a professional reviewing a tablet" style="inset:0"></div>
  <div class="arrow abs" style="left:0;top:253px"><svg width="12" height="12" viewBox="0 0 12 12"><path d="M8 1L3 6l5 5" stroke="#fff" stroke-width="2" fill="none"/></svg></div>
  <div class="arrow abs" style="right:0;top:253px"><svg width="12" height="12" viewBox="0 0 12 12"><path d="M4 1l5 5-5 5" stroke="#fff" stroke-width="2" fill="none"/></svg></div>
  <div class="hero-box abs"><h1>Increasing The Value And Security<br>Of Your Technology Resources</h1></div>
  <div class="hero-btns abs"><span class="btn">Free Consultation</span><span class="btn black">Learn More</span></div>
</section>

<section class="values">
  <div class="value" style="left:207px"><div class="tile"><svg width="46" height="46" viewBox="0 0 46 46" fill="#fff"><circle cx="23" cy="23" r="21" fill="none" stroke="#fff" stroke-width="2"/><circle cx="23" cy="16" r="5"/><path d="M13 33c0-6 4-9 10-9s10 3 10 9z"/></svg></div>CUSTOMER<br>FOCUSED</div>
  <div class="value" style="left:373px"><div class="tile"><svg width="46" height="46" viewBox="0 0 46 46" fill="#fff"><circle cx="20" cy="14" r="7"/><path d="M6 40c0-9 6-14 14-14s14 5 14 14z"/><circle cx="35" cy="30" r="7" fill="none" stroke="#fff" stroke-width="2"/></svg></div>INTEGRITY &amp;<br>ETHICS</div>
  <div class="value" style="left:536px"><div class="tile"><svg width="50" height="46" viewBox="0 0 50 46" fill="#fff"><rect x="8" y="22" width="34" height="4"/><circle cx="14" cy="12" r="5"/><circle cx="36" cy="12" r="5"/><rect x="10" y="26" width="3" height="14"/><rect x="37" y="26" width="3" height="14"/><rect x="20" y="4" width="10" height="8"/></svg></div>PRACTICE<br>ACCOUNTABILITY</div>
  <div class="value" style="left:702px"><div class="tile"><svg width="46" height="46" viewBox="0 0 46 46" fill="#fff"><rect x="6" y="32" width="6" height="8"/><rect x="16" y="26" width="6" height="14"/><rect x="26" y="20" width="6" height="20"/><rect x="36" y="12" width="6" height="28"/><path d="M6 24L20 12l8 4L40 4" stroke="#fff" stroke-width="2" fill="none"/></svg></div>PROFESSIONAL<br>DEVELOPMENT</div>
  <div class="value" style="left:866px"><div class="tile"><svg width="46" height="46" viewBox="0 0 46 46" fill="none" stroke="#fff" stroke-width="2.5"><path d="M8 8h12l-2 14a4 4 0 01-8 0zM14 26v12M9 38h10"/><path d="M26 10h12l-2 14a4 4 0 01-8 0zM32 28v10M27 38h10"/></svg></div>HAVE<br>FUN</div>
</section>

<section class="welcome">
  <h2 class="abs" style="left:210px;top:60px">Welcome To <em>Cardella</em></h2>
  <p class="abs" style="left:210px;top:116px;width:440px">Lorem ipsum dolor sit amet, consectetuer adipiscing elit, sed diam nonummy nibh euismod tincidunt ut laoreet dolore magna aliquam erat volutpat. Ut wisi enim ad minim veniam, quis nostrud exerci tation ullamcorper suscipit lobortis nisl ut aliquip ex ea commodo consequat. Duis autem vel eum.</p>
  <svg class="abs" style="left:210px;top:222px" width="40" height="40" viewBox="0 0 40 40" fill="none" stroke="#6a3fae" stroke-width="2.5"><circle cx="20" cy="20" r="17"/><circle cx="20" cy="20" r="10"/><circle cx="20" cy="20" r="3" fill="#6a3fae"/><path d="M20 20L34 6"/></svg>
  <div class="abs" style="left:262px;top:220px;width:280px">
    <b style="font-family:Roboto,sans-serif;font-size:15px;color:var(--ink)">Our Mission</b>
    <p style="font-size:10px;line-height:16px;margin-top:4px">Partner with customers to increase the value of their technology tools.</p>
  </div>
  <span class="btn abs" style="left:210px;top:306px">Read More</span>
  <div class="ph" role="img" aria-label="Photo of colleagues working together at a laptop in a bright office" style="left:688px;top:52px;width:312px;height:294px;background:linear-gradient(135deg,#e8edf2,#cfd6de 50%,#f2ede6)"></div>
</section>

<section class="services">
  <h2 class="abs" style="left:0;width:1200px;text-align:center;top:46px;color:#fff">Our Services</h2>
  <p class="intro abs">We understand different organizations have different needs. Cardella strives to assist your organization by bringing solutions that are easy to understand and allow the customer to track success. We provide solutions based on the customer's needs and desires.</p>
  <div class="ph" role="img" aria-label="Illustration of healthcare icons in hexagons over a medical background" style="left:210px;top:155px;width:374px;height:208px;background:linear-gradient(135deg,#f4f7fa,#d7e6f0 60%,#b7cde0);border:3px solid rgba(255,255,255,.8)"></div>
  <div class="ph" role="img" aria-label="Photo of a hand touching a digital information technology diagram" style="left:618px;top:155px;width:379px;height:208px;background:linear-gradient(135deg,#2d3f63,#5a77a6 55%,#9fb3d1);border:3px solid rgba(255,255,255,.8)"></div>
  <div class="svc abs" style="left:210px;top:376px">
    <h3>Electronic Health Record (EHR)</h3>
    <ul>
      <li><svg width="10" height="10" viewBox="0 0 10 10"><path d="M1 5l3 3 5-7" stroke="#fff" stroke-width="1.8" fill="none"/></svg>EHR Optimization Services</li>
      <li><svg width="10" height="10" viewBox="0 0 10 10"><path d="M1 5l3 3 5-7" stroke="#fff" stroke-width="1.8" fill="none"/></svg>EHR Implementation</li>
      <li><svg width="10" height="10" viewBox="0 0 10 10"><path d="M1 5l3 3 5-7" stroke="#fff" stroke-width="1.8" fill="none"/></svg>EHR Assessment</li>
      <li><svg width="10" height="10" viewBox="0 0 10 10"><path d="M1 5l3 3 5-7" stroke="#fff" stroke-width="1.8" fill="none"/></svg>EHR Quality Assessment</li>
      <li><svg width="10" height="10" viewBox="0 0 10 10"><path d="M1 5l3 3 5-7" stroke="#fff" stroke-width="1.8" fill="none"/></svg>On-Going EHR Support</li>
    </ul>
    <span class="more">READ MORE</span>
  </div>
  <div class="svc abs" style="left:618px;top:376px">
    <h3>Information Technology</h3>
    <ul>
      <li><svg width="10" height="10" viewBox="0 0 10 10"><path d="M1 5l3 3 5-7" stroke="#fff" stroke-width="1.8" fill="none"/></svg>Risk Assessment</li>
      <li><svg width="10" height="10" viewBox="0 0 10 10"><path d="M1 5l3 3 5-7" stroke="#fff" stroke-width="1.8" fill="none"/></svg>Policy Management and Consulting</li>
      <li><svg width="10" height="10" viewBox="0 0 10 10"><path d="M1 5l3 3 5-7" stroke="#fff" stroke-width="1.8" fill="none"/></svg>Chief Information Officer (CIO) Services</li>
      <li><svg width="10" height="10" viewBox="0 0 10 10"><path d="M1 5l3 3 5-7" stroke="#fff" stroke-width="1.8" fill="none"/></svg>Chief Information Security Officer (CISO) Services</li>
      <li><svg width="10" height="10" viewBox="0 0 10 10"><path d="M1 5l3 3 5-7" stroke="#fff" stroke-width="1.8" fill="none"/></svg>IT Department Evaluation</li>
    </ul>
    <span class="more">READ MORE</span>
  </div>
</section>

<section class="leaders">
  <h2 class="abs" style="left:0;width:1200px;text-align:center;top:50px">Our Leadership <em>Team</em></h2>
  <div class="ph" role="img" aria-label="Portrait photo of the company president in a suit" style="left:210px;top:116px;width:283px;height:291px;background:linear-gradient(160deg,#dfe6ec,#b9c3cc 60%,#4a4f58)"></div>
  <div class="bio abs">
    <b>Grant Ellison, MHA, MBA, CHCIO, CPHIMS</b><br>President and CEO
    <p style="margin-top:8px">As the Founder and CEO of Cardella, Grant has been working in the technology industry for over 25 years with extensive experience in healthcare and IT. As a consultant Grant held multiple roles including CIO and CISO. Over the years, Grant has been the executive sponsor of multiple electronic health record (EHR) implementations. He has created and nurtured numerous successful.</p>
  </div>
  <div class="thumb" style="left:520px"><div class="ph" role="img" aria-label="Small portrait photo of Grant Ellison" style="background:linear-gradient(160deg,#e3e8ee,#8e97a3);border:3px solid var(--purple)"></div>GRANT ELLISON</div>
  <div class="thumb" style="left:686px"><div class="ph" role="img" aria-label="Small portrait photo of Dana Whitfield" style="background:linear-gradient(160deg,#eceff2,#7b838d)"></div>DANA WHITFIELD</div>
</section>

<section class="clients">
  <div class="ph" role="img" aria-label="Dimmed photo of a group meeting in an office" style="inset:0;background:linear-gradient(90deg,rgba(30,30,34,.9),rgba(60,60,68,.85) 50%,rgba(30,30,34,.9))"></div>
  <h2 class="abs" style="left:0;width:1200px;text-align:center;top:48px;color:#fff">What Clients Say <em>About Us</em></h2>
  <svg class="abs" style="left:178px;top:208px" width="12" height="16" viewBox="0 0 12 16"><path d="M9 2L3 8l6 6" stroke="#aaa" stroke-width="2" fill="none"/></svg>
  <svg class="abs" style="left:1003px;top:208px" width="12" height="16" viewBox="0 0 12 16"><path d="M3 2l6 6-6 6" stroke="#aaa" stroke-width="2" fill="none"/></svg>
  <div class="quote" style="left:210px"><div class="ph" role="img" aria-label="Client portrait photo" style="background:linear-gradient(160deg,#e9e4df,#9b8f86)"></div>Lorem ipsum dolor sit amet, consectetuer adipiscing elit, sed diam nonummy nibh euismod tincidunt ut laoreet dolore magna aliquam erat volutpat. Ut wisi enim ad minim veniam, quis nostrud exerci tation ullamcorper.<div class="who">MARIA LENZ <span style="color:var(--ink)">★★★★★</span></div></div>
  <div class="quote" style="left:632px;width:345px"><div class="ph" role="img" aria-label="Client portrait photo" style="background:linear-gradient(160deg,#e6eaee,#7e8894)"></div>Lorem ipsum dolor sit amet, consectetuer adipiscing elit, sed diam nonummy nibh euismod tincidunt ut laoreet dolore magna aliquam erat volutpat. Ut wisi enim ad minim veniam, quis nostrud exerci tation ullamcorper.<div class="who">MARIA LENZ <span style="color:var(--ink)">★★★★★</span></div></div>
</section>

<section class="approach">
  <div class="left abs" role="img" aria-label="Purple-tinted photo of medical staff in a hospital"></div>
  <div class="abs" style="left:210px;top:183px;display:flex;align-items:center;gap:10px;font-family:Poppins,sans-serif;font-weight:600;font-size:40px;color:#fff"><i style="width:14px;height:14px;background:#fff;display:block"></i>Cardella</div>
  <div class="pill" style="top:28px"><div class="sq"><svg width="46" height="34" viewBox="0 0 46 34" fill="#fff"><circle cx="23" cy="8" r="6"/><circle cx="9" cy="12" r="4"/><circle cx="37" cy="12" r="4"/><path d="M13 30c0-8 4-12 10-12s10 4 10 12zM1 30c0-6 3-9 8-9l2 1-2 8zM45 30c0-6-3-9-8-9l-2 1 2 8z"/></svg></div><p>Understand and get to know<br>customer and their needs</p></div>
  <div class="pill" style="top:168px"><div class="sq"><svg width="48" height="30" viewBox="0 0 48 30" fill="none" stroke="#fff" stroke-width="2.5"><path d="M2 8l10-4 10 5 8-3 16 6M2 8v12l8 0 12 8 6-4 10 4 8-8v-10"/><path d="M20 14l8 6M24 12l8 6"/></svg></div><p>Committed to be a partner,<br>not vendor</p></div>
  <div class="pill" style="top:307px"><div class="sq"><svg width="44" height="44" viewBox="0 0 44 44" fill="#fff"><circle cx="22" cy="14" r="6"/><path d="M12 30c0-7 4-10 10-10s10 3 10 10z"/><circle cx="5" cy="22" r="4"/><circle cx="39" cy="22" r="4"/><circle cx="22" cy="40" r="4"/></svg></div><p>Provide simplified change<br>management expertise</p></div>
</section>

<section class="blog">
  <h2 class="abs" style="left:0;width:1200px;text-align:center;top:40px">Latest <em>Blog</em></h2>
  <svg class="abs" style="left:166px;top:240px" width="12" height="16" viewBox="0 0 12 16"><path d="M9 2L3 8l6 6" stroke="#999" stroke-width="2" fill="none"/></svg>
  <svg class="abs" style="left:1018px;top:240px" width="12" height="16" viewBox="0 0 12 16"><path d="M3 2l6 6-6 6" stroke="#999" stroke-width="2" fill="none"/></svg>
  <div class="card" style="left:210px"><div class="ph" role="img" aria-label="Photo of healthcare professionals in a meeting" style="background:linear-gradient(135deg,#c9d2da,#8a96a3)"></div><div class="date">29<small>OCT</small></div><h4>sed diam nonummy nibh euismod tincidunt ut laoreet</h4><p>ore exerci tation ullamcorper suscipit lobortis nisl ut aliquip ex ea commodo consequat. Duis autem vel eum</p><i class="corner"></i></div>
  <div class="card" style="left:480px"><div class="ph" role="img" aria-label="Illustration of blue molecular structures" style="background:linear-gradient(135deg,#e8f0f6,#9fbad0 60%,#5f85a8)"></div><div class="date">29<small>OCT</small></div><h4>sed diam nonummy nibh euismod tincidunt ut laoreet</h4><p>ore exerci tation ullamcorper suscipit lobortis nisl ut aliquip ex ea commodo consequat. Duis autem vel eum</p><i class="corner p"></i></div>
  <div class="card" style="left:750px"><div class="ph" role="img" aria-label="Photo of a doctor consulting with a patient and family" style="background:linear-gradient(135deg,#e6e2dc,#b4aca2 60%,#6e6a66)"></div><div class="date">29<small>OCT</small></div><h4>sed diam nonummy nibh euismod tincidunt ut laoreet</h4><p>ore exerci tation ullamcorper suscipit lobortis nisl ut aliquip ex ea commodo consequat. Duis autem vel eum</p><i class="corner"></i></div>
  <span class="btn abs" style="left:545px;top:436px;padding:10px 22px">View More</span>
</section>

<footer class="site-footer">
  <h3 class="abs" style="left:210px;top:38px">Send Us A Message</h3>
  <div class="abs" style="left:210px;top:70px;width:420px;height:1px;background:#444"></div>
  <div class="field" style="top:92px">Your Name</div>
  <div class="field" style="top:130px">Email Address</div>
  <div class="field" style="top:168px">Phone Number</div>
  <div class="field" style="top:206px">Subject</div>
  <div class="field" style="left:435px;top:92px;width:198px;height:144px">Message</div>
  <span class="btn abs" style="left:210px;top:248px;padding:9px 20px">Submit Now</span>

  <h3 class="abs" style="left:710px;top:38px">Contact Details</h3>
  <div class="abs" style="left:710px;top:70px;width:280px;height:1px;background:#444"></div>
  <p class="abs" style="left:710px;top:82px;width:280px;font-size:10px;line-height:16px;color:#bbb">Lorem ipsum dolor sit amet, consectetur adipiscing. Aenean urna magna, porta eu in, fringilla venenat.</p>
  <div class="contact-row" style="top:128px"><svg width="20" height="22" viewBox="0 0 20 22" fill="#fff"><path d="M10 1a7 7 0 017 7c0 5-7 13-7 13S3 13 3 8a7 7 0 017-7z"/><circle cx="10" cy="8" r="2.5" fill="#222"/></svg><div><b>LOCATION</b><span>9806 Lorem Dolor Sit Amet, Toronto</span></div></div>
  <div class="contact-row" style="top:176px"><svg width="20" height="20" viewBox="0 0 24 24" fill="#fff"><path d="M6 2l4 5-2 3c1 3 4 6 7 7l3-2 5 4-3 4C9 22 1 13 2 5z"/></svg><div><b>PHONE</b><span>555-014-2290</span></div></div>
  <div class="contact-row" style="top:224px"><svg width="20" height="16" viewBox="0 0 20 16" fill="none" stroke="#fff" stroke-width="2"><rect x="1" y="1" width="18" height="14"/><path d="M1 1l9 8 9-8"/></svg><div><b>EMAIL</b><span>gellison@cardellahealth.example</span></div></div>

  <div class="bottom-bar abs">
    <span class="abs" style="left:210px;top:12px">© COPYRIGHT 2018 CARDELLA. ALL RIGHTS RESERVED.</span>
    <div class="abs" style="right:210px;top:8px;display:flex;align-items:center;gap:10px;font-weight:600">FOLLOW US ON <div class="social"><i></i><i></i><i></i><i></i></div></div>
  </div>
</footer>

</body>
</html>
```